Skincare Cleanser Bottle Label

New product launch of a mint facial cleanser.
Brand is called Dorvelle.
Product will be called Lunara.
Looking for a label design that can be printed using silk screening.
High gloss white plastic bottle. 8oz. White push pump top.
Clinical skincare brand, professional image, sold in medical spas.

Target Market(s)

Women Age 20-65

Industry/Entity Type

Health And Wellness

Font styles to use
Serif
Sans Serif

Requirements
Must have
• Dorvelle brand name in the orignal font.
Should not have
• Multiple colours.

```html
<!DOCTYPE html>
<html lang="en">
<head>
<meta charset="utf-8">
<title>Dorvelle Lunara Mint Facial Cleanser Label</title>
<link href="https://fonts.googleapis.com/css2?family=Josefin+Sans:wght@300;400&display=swap" rel="stylesheet">
<style>
  :root {
    --paper: #ffffff;
    --ink: #141414;
    --ink-soft: #2a2a2a;
    --silver-light: #f4f4f4;
    --silver-mid: #d6d6d6;
    --silver-dark: #b9b9b9;
    --leaf-light: #6cc04a;
    --leaf-dark: #2f7d27;
  }
  * { margin: 0; padding: 0; box-sizing: border-box; }
  html, body { width: 738px; height: 1200px; overflow: hidden; background: var(--paper); }
  .label {
    position: relative;
    width: 738px;
    height: 1200px;
    background: var(--paper);
    color: var(--ink);
    font-family: "Josefin Sans", sans-serif;
    font-weight: 300;
  }
  .brand {
    position: absolute;
    left: 0; width: 736px;
    top: 62px;
    text-align: center;
    font-size: 44px;
    font-weight: 400;
    letter-spacing: 1px;
    line-height: 1;
    color: var(--ink);
  }
  .accent-bar {
    position: absolute;
    left: 181px; top: 234px;
    width: 12px; height: 627px;
    background: repeating-linear-gradient(90deg,
      var(--silver-dark) 0 2px, var(--silver-light) 2px 4px, var(--silver-mid) 4px 6px);
  }
  .product-name, .product-type span {
    position: absolute;
    left: 205px;
    line-height: 1;
    white-space: nowrap;
    font-weight: 300;
  }
  .product-name { top: 226px; font-size: 102px; letter-spacing: 1px; }
  .product-type span { font-size: 86px; letter-spacing: 1px; }
  .product-type .line-1 { top: 402px; }
  .product-type .line-2 { top: 504px; }
  .product-type .line-3 { top: 612px; }
  .description {
    position: absolute;
    left: 201px; top: 721px;
    width: 355px; height: 140px;
    padding: 14px 12px 0 12px;
    background: repeating-linear-gradient(90deg,
      var(--silver-light) 0 10px, var(--silver-mid) 18px, var(--silver-light) 28px,
      var(--silver-dark) 34px, var(--silver-light) 44px);
    font-size: 16px;
    line-height: 30px;
    color: var(--ink-soft);
    font-weight: 400;
  }
  .mint-leaf {
    position: absolute;
    left: 236px; top: 906px;
    width: 249px; height: 190px;
    border-radius: 60% 40% 55% 45% / 55% 50% 50% 45%;
    background: radial-gradient(ellipse at 45% 40%, var(--leaf-light), var(--leaf-dark));
  }
  .volume {
    position: absolute;
    left: 0; width: 730px;
    top: 1143px;
    text-align: center;
    font-size: 20px;
    font-weight: 400;
    line-height: 1;
  }
</style>
</head>
<body>
  <main class="label">
    <div class="brand">dorvelle</div>
    <div class="accent-bar"></div>
    <h1 class="product-name">LUNARA</h1>
    <h2 class="product-type">
      <span class="line-1">MINT</span>
      <span class="line-2">FACIAL</span>
      <span class="line-3">CLEANSER</span>
    </h2>
    <p class="description">Lorem Ipsum is simply dummy text of the printing and typesetting industry. Lorem Ipsum has been the industry's standard dummy text ever since the 1500s.</p>
    <div class="mint-leaf" role="img" aria-label="Photograph of a fresh mint sprig"></div>
    <div class="volume">8 OZ</div>
  </main>
</body>
</html>
```